Free wellness evaluation

We need an A5 flyer designing using both sides The front side needs to contain most of the information about the free wellness evaluation with Voucher clearly Displayed,we needs to demonstrate that we are very professional company offering a unique service

Industry/Entity Type

Wellness

```html
<!DOCTYPE html>
<html lang="en">
<head>
<meta charset="utf-8">
<title>Free wellness evaluation flyer</title>
<link rel="stylesheet" href="https://fonts.googleapis.com/css2?family=Fira+Sans:ital,wght@0,400;0,700;1,400;1,500;1,600;1,700&display=swap">
<style>
  :root {
    --backdrop: #0c0e0e;
    --paper: #ffffff;
    --brand-green: #4fd40f;
    --band-dark: #1c1c1c;
    --band-text: #d0d0d0;
    --accent-orange: #f57f0c;
    --body-text: #111111;
    --rule: #bdbdbd;
  }
  * { margin: 0; padding: 0; box-sizing: border-box; }
  html, body { width: 1200px; height: 1000px; overflow: hidden; }
  body {
    background: var(--backdrop);
    font-family: "Fira Sans", Arial, sans-serif;
    position: relative;
  }
  .flyer {
    position: absolute;
    left: 289px; top: 60px;
    width: 620px; height: 880px;
    background: var(--paper);
  }
  .brand-header { position: relative; height: 130px; }
  .brand-dot {
    position: absolute; left: 21px; top: 27px;
    width: 76px; height: 76px; border-radius: 50%;
    background: var(--brand-green);
  }
  .brand-name {
    position: absolute; left: 111px; top: 24px;
    font-weight: 700; font-size: 52px; letter-spacing: 1px;
    color: var(--brand-green); line-height: 1;
  }
  .brand-tagline {
    position: absolute; left: 116px; top: 80px;
    font-style: italic; font-size: 21.5px;
    color: var(--brand-green);
  }
  .title-band {
    height: 55px; background: var(--band-dark);
    padding-left: 22px;
  }
  .title-band h1 {
    font-style: italic; font-weight: 600; font-size: 35.5px;
    color: var(--band-text); line-height: 58px; letter-spacing: -0.5px;
  }
  .content { padding: 62px 0 0 54px; }
  .content h2 {
    font-style: italic; font-weight: 500; font-size: 29px;
    color: var(--accent-orange); margin-bottom: 35px;
  }
  .benefits { list-style: none; }
  .benefit {
    position: relative; padding-left: 45px;
    font-style: italic; font-size: 17px; line-height: 28px;
    letter-spacing: -0.15px;
    color: var(--body-text);
  }
  .benefit svg { position: absolute; left: 20px; top: 9px; }
  .divider {
    width: 334px; height: 1px; background: var(--rule);
    margin: 39px 0 33px 92px;
  }
</style>
</head>
<body>
  <main class="flyer">
    <header class="brand-header">
      <span class="brand-dot"></span>
      <div class="brand-name">VITAL STRIDE</div>
      <div class="brand-tagline">Personal Training &amp; Nutritional Specialist</div>
    </header>
    <div class="title-band"><h1>Free wellness evaluation</h1></div>
    <section class="content">
      <h2>Book a free wellness evaluation</h2>
      <ul class="benefits">
        <li class="benefit">
          <svg width="9" height="10" viewBox="0 0 9 10"><path d="M1 1l5 4-5 4" fill="none" stroke="#4fd40f" stroke-width="2.6"/></svg>
          Who can book free wellness evaluation either book<br>an individual wellness check for yourself or book a family<br>wellness evaluation you can even book an assessment<br>for you and your friends at no charge.
        </li>
        <li class="divider" aria-hidden="true"></li>
        <li class="benefit">
          <svg width="9" height="10" viewBox="0 0 9 10"><path d="M1 1l5 4-5 4" fill="none" stroke="#4fd40f" stroke-width="2.6"/></svg>
          Wellness evaluations are ideal for individuals or families<br>that are concerned or interested in their diet and exercising<br>habits and may want some advice.
        </li>
        <li class="divider" aria-hidden="true"></li>
        <li class="benefit">
          <svg width="9" height="10" viewBox="0 0 9 10"><path d="M1 1l5 4-5 4" fill="none" stroke="#4fd40f" stroke-width="2.6"/></svg>
          Free wellness evaluation is also ideal for individuals<br>that are Fed up with fad diets, are interested in a nutritional<br>approach which will help you lose weight and the key point<br>offering advice and support to keep weight at the level<br>you are comfortable with.
        </li>
      </ul>
    </section>
  </main>
</body>
</html>
```